International Firefighter Competition Needs New Website that Looks Like It's a Global Sportin...

The Summit Relay is held globally and sees thousands of firefighters competing on an obstacle course known as the toughest two minutes in sports. This year the organization received a makeover with new logo and new look of our challenge course. We also introduced the Summit Relay Circuit (known as the SRC). We envision a new website that inspires our next generation of competitors! It's time to wow them visually and to make them feel that this exciting sport proudly represents them as our global heroes that protect each and every one of us in a moments notice! NOTE: Photos provided are just for you to use as placeholders. TO SEE A VIDEO OF OUR EVENT: https://clipvault-example.net/482617305

NOTE: In 2023 we sub-divided the U.S. into 5 new regions for the SRC: Summit Relay Circuit. I've now added these logos in the event a designer sees a vision of integrating these.

Target Market(s)

Firefighters and Sponsors

Coding

Coded - Design and coding required

Requirements
Must have
• Rival other major sporting event websites. See attached samples.
Nice to have
• No suggestions. We truly are open to creativity.
Should not have
• Too firefighter looking. Needs to be the perfect blend of promoting our firefighters as athletes in our sport.

```html
<!DOCTYPE html>
<html lang="en">
<head>
<meta charset="utf-8">
<title>Summit Relay</title>
<link href="https://fonts.googleapis.com/css2?family=Oswald:wght@400;500;600;700&display=swap" rel="stylesheet">
<style>
  :root {
    --blue: #2b8fd6;
    --blue-deep: #1f7cc4;
    --navy: #0b2a4a;
    --red: #d3323e;
    --ink: #050a14;
    --white: #ffffff;
    --grey-text: #3a3a3a;
  }
  * { margin: 0; padding: 0; box-sizing: border-box; }
  html, body { width: 1200px; height: 692px; overflow: hidden; background: var(--white); }
  .page { position: relative; width: 1200px; height: 692px; font-family: "Oswald", sans-serif; }

  .site-header { position: absolute; top: 0; left: 0; width: 1200px; height: 88px; background: var(--white); z-index: 3; }
  .brand-name {
    position: absolute; left: 148px; top: 26px; height: 36px;
    font-family: "Oswald", sans-serif; font-weight: 700; font-size: 26px; line-height: 36px;
    color: var(--navy); text-transform: uppercase; letter-spacing: .5px; white-space: nowrap;
  }
  .main-nav a {
    position: absolute; top: 35px; font-size: 18px; font-weight: 500; color: var(--blue);
    text-decoration: none; text-transform: uppercase; line-height: 26px; white-space: nowrap;
  }
  .main-nav a.is-active { color: var(--red); }
  .main-nav a.is-active::before {
    content: ""; position: absolute; left: 0; right: 0; top: -6px; height: 3px; background: var(--blue);
  }
  .league-mark {
    position: absolute; left: 970px; top: 30px; font-weight: 700; font-size: 26px; line-height: 36px; color: var(--blue); letter-spacing: 1px;
  }

  .hero { position: absolute; top: 88px; left: 0; width: 1200px; height: 550px; background: var(--ink); overflow: hidden; }
  .hero-photo {
    position: absolute; inset: 0;
    background:
      radial-gradient(ellipse 260px 330px at 400px 300px, #2a2f38 0%, #14181f 55%, transparent 100%),
      radial-gradient(ellipse 500px 420px at 250px 260px, #1a2028 0%, #0a0f18 70%, var(--ink) 100%);
  }
  .hero-panel { position: absolute; inset: 0; }
  .hero-copy { position: absolute; left: 748px; top: 150px; width: 400px; height: 260px; color: var(--white); }
  .hero-title {
    font-weight: 700; font-style: italic; font-size: 60px; line-height: 61px; text-transform: uppercase; letter-spacing: -.5px;
  }
  .hero-text { margin-top: 22px; font-family: Arial, Helvetica, sans-serif; font-size: 15px; line-height: 18px; width: 290px; }
  .cta {
    position: absolute; left: 0; top: 204px; width: 149px; height: 42px; display: flex;
    border: 2px solid var(--white); text-decoration: none;
  }
  .cta-label {
    flex: 1; background: var(--navy); color: var(--white); font-size: 18px; font-weight: 500;
    display: flex; align-items: center; justify-content: center; text-transform: uppercase;
  }
  .cta-arrow { width: 33px; background: var(--red); display: flex; align-items: center; justify-content: center; }

  .social-links { position: absolute; left: 20px; top: 215px; display: flex; flex-direction: column; gap: 12px; }
  .social-links span { color: var(--white); font-size: 11px; font-weight: 500; text-transform: uppercase; letter-spacing: .5px; }

  .site-footer { position: absolute; top: 638px; left: 0; width: 1200px; height: 54px; background: var(--white); }
  .call-band { position: absolute; left: 0; top: 0; }
  .call-text {
    position: absolute; left: 30px; top: 0; height: 54px; display: flex; align-items: center; gap: 10px;
    color: var(--white); font-weight: 500; font-size: 22px; text-transform: uppercase; white-space: nowrap;
  }
  .video-link { position: absolute; left: 347px; top: 0; height: 54px; display: flex; align-items: center; gap: 8px; }
  .video-service { font-size: 14px; font-weight: 600; color: var(--red); }
  .video-label { font-size: 14px; color: var(--grey-text); text-transform: uppercase; }
  .copyright { position: absolute; right: 148px; top: 0; line-height: 54px; font-size: 14px; color: var(--grey-text); text-transform: uppercase; white-space: nowrap; }
</style>
</head>
<body>
<div class="page">

  <header class="site-header">
    <div class="brand-name">Summit Relay</div>
    <nav class="main-nav">
      <a class="is-active" href="#" style="left:386px">Home</a>
      <a href="#" style="left:460px">About Us</a>
      <a href="#" style="left:566px">Our Events</a>
      <a href="#" style="left:681px">Training</a>
      <a href="#" style="left:779px">News</a>
      <a href="#" style="left:853px">Contact</a>
    </nav>
    <div class="league-mark">SRC</div>
  </header>

  <section class="hero">
    <div class="hero-photo" role="img" aria-label="Photo of a firefighter in helmet and turnout gear standing with arms crossed against a dark wall"></div>

    <svg class="hero-panel" width="1200" height="550" viewBox="0 0 1200 550">
      <defs>
        <linearGradient id="panel-fade" x1="0" y1="0" x2="1" y2="0.35">
          <stop offset="0" stop-color="#2b8fd6"/>
          <stop offset="0.4" stop-color="#3a86cf"/>
          <stop offset="0.75" stop-color="#9a4a70"/>
          <stop offset="1" stop-color="#cf343f"/>
        </linearGradient>
      </defs>
      <polygon points="650,281 569,476 591,476" fill="#d3323e"/>
      <polygon points="750,47 1200,47 1200,476 591,476" fill="url(#panel-fade)"/>
    </svg>

    <div class="hero-copy">
      <h1 class="hero-title">Summit<br>Relay</h1>
      <p class="hero-text">Lorem ipsum dolor sit amet, consectetur adipiscing elit, sed do eiusmod temp.</p>
      <a class="cta" href="#">
        <span class="cta-label">Our Events</span>
        <span class="cta-arrow">
          <svg width="20" height="16" viewBox="0 0 20 16"><path d="M1 8h16M10 1l7 7-7 7" fill="none" stroke="#fff" stroke-width="2.6" stroke-linecap="round" stroke-linejoin="round"/></svg>
        </span>
      </a>
    </div>

    <div class="social-links">
      <span>Pixo</span>
      <span>Chirp</span>
      <span>Linka</span>
    </div>
  </section>

  <footer class="site-footer">
    <svg class="call-band" width="334" height="54" viewBox="0 0 334 54"><polygon points="0,0 334,0 301,54 0,54" fill="#d3323e"/></svg>
    <div class="call-text">
      <svg width="16" height="16" viewBox="0 0 24 24"><path d="M6.6 10.8c1.4 2.8 3.8 5.1 6.6 6.6l2.2-2.2c.3-.3.7-.4 1-.2 1.1.4 2.3.6 3.6.6.6 0 1 .4 1 1V20c0 .6-.4 1-1 1C10.6 21 3 13.4 3 4c0-.6.4-1 1-1h3.5c.6 0 1 .4 1 1 0 1.3.2 2.5.6 3.6.1.3 0 .7-.2 1z" fill="#fff"/></svg>
      <span>Call us: 123 456 7890</span>
    </div>
    <div class="video-link">
      <span class="video-service">Streamly</span>
      <span class="video-label">Our Events</span>
    </div>
    <div class="copyright">Copyright © 2023 All rights reserved.</div>
  </footer>

</div>
</body>
</html>
```